Spiritual Support flyer design

I offer a range of spiritual support options from a drop in group to meditation. I work alone in two locations, one at home and the other in the local town centre therapy centre. I do not want people to be confused about where to go for each item so thought one side could be the town centre group and the other side of the leaflet could be the things I offer from home. I need to find a way to present a list of things I do and make it look inviting so people want to contact me. I want it to feel inspirational, uplifting, light hearted, with a gentle feel of support or coming home to somewhere safe. The leaflet needs to look eye catching as it will be where there are many other leaflets the same size (A5). I love purples, as they tend to be spiritual colours or the look below of light bursting through the clouds seems appropriate picture wise. I do not have a logo.
The title can be Amber Lantern. On one side I would like to introduce a Spiritual Experiences drop-in group held at the Pebble Hall Centre, Colchester 1-2pm every four weeks to share spiritual experiences with others. I can give you more words for that when you are ready. The other side needs to feature the things I offer from my own home which are: Spiritual Counselling, Private email guidance, Meditation one to one, and Amber Lantern Days, which are like a days retreat. It might be a good idea to mention prices but not in an obvious way, so have that just readable in small print.

```html
<!DOCTYPE html>
<html lang="en">
<head>
<meta charset="utf-8">
<title>Spiritual Support Flyers</title>
<link rel="stylesheet" href="https://fonts.googleapis.com/css2?family=Cabin:wght@600&family=Satisfy&family=Open+Sans:wght@400&family=Noto+Serif:ital@1&family=Lato:wght@400&display=swap">
<style>
:root{
  --stage:#e9e5df;
  --paper:#f6f5f9;
  --purple:#6a5aa3;
  --purple-deep:#5a4a94;
  --lavender:#c9c2e2;
  --ink:#4a4a55;
  --ink-soft:#5c5c66;
  --white:#ffffff;
}
*{margin:0;padding:0;box-sizing:border-box}
html,body{width:1200px;height:942px;overflow:hidden;background:var(--stage)}
.stage{position:relative;width:1200px;height:942px}
.flyer{position:absolute;width:528px;height:743px;background:linear-gradient(180deg,#eeedf4 0%,var(--paper) 30%,#fbfbfd 100%);box-shadow:0 4px 14px rgba(0,0,0,.25);overflow:hidden;color:var(--ink)}
.flyer--experiences{left:52px;top:57px}
.flyer--counselling{left:623px;top:128px}
.title{position:absolute;left:70px;top:52px;font-family:'Cabin',sans-serif;font-weight:600;color:var(--purple);line-height:1}
.title__main{display:block;font-size:34px;letter-spacing:1px}
.title__sub{display:block;font-size:19px;letter-spacing:1px;margin-top:8px;padding-left:4px}
.venue{position:absolute;left:314px;top:16px;width:206px;height:87px;border:1px dashed #d3d0de;background:rgba(255,255,255,.6);font-family:'Lato',sans-serif;color:var(--ink-soft);text-align:center;padding-top:10px;font-size:13px;line-height:19px}
.venue__head{font-size:14px;letter-spacing:.5px}
.venue__fee{position:absolute;right:8px;bottom:6px;font-size:10px}
.venue--small .venue__addr{font-size:11.5px}
.photo{position:absolute;left:0;width:528px}
.photo--hands{top:118px;height:300px;background:radial-gradient(ellipse at 55% 50%,#c88e78 0%,#d9a994 35%,#e7d3d0 70%,#ddd6e6 100%)}
.photo--meditation{top:118px;height:290px;background:linear-gradient(90deg,#c9d6da 0%,#d8e0e3 30%,#e3c9dc 60%,#d9b7d3 80%,#c5bfd6 100%)}
.waves{position:absolute;left:0;top:0;width:528px;height:743px}
.invite{position:absolute;left:24px;top:430px;right:20px}
.invite__names{font-family:'Satisfy',cursive;font-size:25px;color:var(--purple)}
.invite__tag{font-family:'Open Sans',sans-serif;font-size:15px;letter-spacing:.5px;color:var(--ink)}
.invite__lead{font-family:'Open Sans',sans-serif;font-size:12.5px;line-height:16px;margin-top:2px}
.about{position:absolute;left:38px;top:520px;right:42px;font-family:'Noto Serif',serif;font-style:italic;font-size:11px;line-height:15px;color:var(--ink-soft);text-align:justify}
.about p{margin-bottom:5px}
.about .person{color:var(--purple);padding-left:16px}
.about .link{color:var(--purple)}
.rule{position:absolute;left:0;right:0;top:693px;height:2px;background:var(--purple)}
.contact-band{position:absolute;left:0;right:0;top:700px;height:43px;background:linear-gradient(90deg,var(--purple-deep),#7a6cb3 50%,var(--purple-deep));display:flex;justify-content:center;align-items:center;gap:44px;font-family:'Open Sans',sans-serif;font-size:15px;color:var(--white)}
.contact-band__item{display:flex;align-items:center;gap:9px}
.contact-band__item svg{width:16px;height:16px}
.offer{position:absolute;left:28px;top:432px;right:20px}
.offer__title{font-family:'Satisfy',cursive;font-size:27px;color:var(--purple)}
.offer__lead{font-family:'Open Sans',sans-serif;font-size:13px;line-height:20px;color:var(--ink);margin-top:2px}
.price{color:var(--purple)}
.services{position:absolute;left:52px;top:528px;list-style:none;font-family:'Open Sans',sans-serif;font-size:13px;line-height:22px;color:var(--ink)}
.services li{display:flex;align-items:center;gap:8px}
.services svg{width:12px;height:12px;flex:none}
.booking{position:absolute;left:0;right:0;top:662px;text-align:center;font-family:'Noto Serif',serif;font-style:italic;font-size:13px;color:var(--ink-soft)}
.booking__url{font-family:'Open Sans',sans-serif;font-style:normal;font-size:17px;color:var(--purple);margin-left:6px}
</style>
</head>
<body>
<main class="stage">

  <section class="flyer flyer--experiences">
    <div class="photo photo--hands" role="img" aria-label="Photo of several hands stacked together in support"></div>
    <svg class="waves" viewBox="0 0 528 743" aria-hidden="true">
      <path d="M0,0H528V118C430,118 340,148 250,160C150,172 60,158 0,140Z" fill="#f1f0f6"/>
      <path d="M0,140C60,158 150,172 250,160C340,148 430,118 528,118V128C430,130 340,160 250,170C150,182 60,168 0,150Z" fill="#c9c2e2"/>
      <path d="M210,158C330,140 430,112 528,118V138C440,132 340,155 210,158Z" fill="#6a5aa3"/>
      <path d="M0,372C90,405 200,420 320,412C420,405 480,390 528,385V743H0Z" fill="#f8f8fb"/>
      <path d="M0,372C90,405 200,420 320,412C420,405 480,390 528,385V396C480,402 420,414 320,420C200,428 90,418 0,390Z" fill="#6a5aa3"/>
      <path d="M0,390C90,418 200,428 320,420C420,414 480,402 528,396V404C470,412 400,426 310,430C200,434 90,426 0,400Z" fill="#c9c2e2"/>
    </svg>
    <h1 class="title"><span class="title__main">SPIRITUAL</span><span class="title__sub">EXPERIENCES</span></h1>
    <div class="venue">
      <div class="venue__head">A DROP-IN GROUP</div>
      <div class="venue__addr">at The Pebble Hall Centre,</div>
      <div class="venue__addr">12 Willow Lane, Colchester</div>
      <div class="venue__fee">Contribution: £5</div>
    </div>
    <div class="invite">
      <div><span class="invite__names">Rosa and Mae</span> <span class="invite__tag">INVITE YOU</span></div>
      <p class="invite__lead">to drop in and share any spiritual experiences you may have had, enlightened moments, or developing spiritual gifts, in a supportive environment.</p>
    </div>
    <div class="about">
      <p>Perhaps you feel that you are the only one experiencing what you do and would like to talk about it, or listen to others experiences. In the group you can share with like-minded souls for personal development and inspiration.</p>
      <p><span class="person">Rosa Vale</span> – has loved all things spiritual from an early age and provides email consultations, spiritual counselling, and amber lantern days <span class="link">rosa.vale@lanternmail.com 01632 960418</span></p>
      <p><span class="person">Mae Hollis</span> – had a spiritual awakening and became open to angels, is sensitive to energies, and has been on a pathway of self-discovery ever since. She enjoys emotionally supporting others on their life journey.<br><span class="link">Please contact Rosa for future dates.</span></p>
    </div>
    <div class="rule"></div>
    <footer class="contact-band">
      <span class="contact-band__item"><svg viewBox="0 0 16 16"><circle cx="8" cy="8" r="8" fill="#fff"/><rect x="4" y="5" width="8" height="6" fill="#5a4a94"/><path d="M4,5L8,8.5L12,5" stroke="#fff" fill="none" stroke-width="1"/></svg>rosa.vale@lanternmail.com</span>
      <span class="contact-band__item"><svg viewBox="0 0 16 16"><circle cx="8" cy="8" r="8" fill="#fff"/><path d="M5.5,4.5l1.5,0l0.8,2l-1,0.8c0.5,1,1.2,1.7,2.2,2.2l0.8-1l2,0.8l0,1.5c-3.5,0.5-7-3-6.3-6.3z" fill="#5a4a94"/></svg>01632 960418</span>
    </footer>
  </section>

  <section class="flyer flyer--counselling">
    <div class="photo photo--meditation" role="img" aria-label="Photo of a woman seated cross-legged meditating in a bright room"></div>
    <svg class="waves" viewBox="0 0 528 743" aria-hidden="true">
      <path d="M0,0H528V118C430,118 340,148 250,160C150,172 60,158 0,140Z" fill="#f1f0f6"/>
      <path d="M0,140C60,158 150,172 250,160C340,148 430,118 528,118V128C430,130 340,160 250,170C150,182 60,168 0,150Z" fill="#c9c2e2"/>
      <path d="M210,158C330,140 430,112 528,118V138C440,132 340,155 210,158Z" fill="#6a5aa3"/>
      <path d="M0,372C90,405 200,420 320,412C420,405 480,390 528,385V743H0Z" fill="#f8f8fb"/>
      <path d="M0,372C90,405 200,420 320,412C420,405 480,390 528,385V396C480,402 420,414 320,420C200,428 90,418 0,390Z" fill="#6a5aa3"/>
      <path d="M0,390C90,418 200,428 320,420C420,414 480,402 528,396V404C470,412 400,426 310,430C200,434 90,426 0,400Z" fill="#c9c2e2"/>
    </svg>
    <h1 class="title"><span class="title__main">SPIRITUAL</span><span class="title__sub">COUNSELLING</span></h1>
    <div class="venue venue--small">
      <div class="venue__head">AMBER LANTERN</div>
      <div class="venue__addr">at The Meditation Room,</div>
      <div class="venue__addr">41 Heron Close, Colchester CO9 4QX</div>
    </div>
    <div class="offer">
      <h2 class="offer__title">Spiritual Counselling</h2>
      <p class="offer__lead">Up to an hours confidential one to one support and assistance £45<br>Private email guidance</p>
    </div>
    <ul class="services">
      <li><svg viewBox="0 0 12 12"><circle cx="6" cy="6" r="6" fill="#6a5aa3"/><path d="M5,3.5L7.5,6L5,8.5" stroke="#fff" stroke-width="1.5" fill="none"/></svg>Response within 24 hours or sooner <span class="price">£45</span></li>
      <li><svg viewBox="0 0 12 12"><circle cx="6" cy="6" r="6" fill="#6a5aa3"/><path d="M5,3.5L7.5,6L5,8.5" stroke="#fff" stroke-width="1.5" fill="none"/></svg>Meditation One to One</li>
      <li><svg viewBox="0 0 12 12"><circle cx="6" cy="6" r="6" fill="#6a5aa3"/><path d="M5,3.5L7.5,6L5,8.5" stroke="#fff" stroke-width="1.5" fill="none"/></svg>Bigger or advanced assistance to develop your practice <span class="price">£45</span></li>
      <li><svg viewBox="0 0 12 12"><circle cx="6" cy="6" r="6" fill="#6a5aa3"/><path d="M5,3.5L7.5,6L5,8.5" stroke="#fff" stroke-width="1.5" fill="none"/></svg>Amber Lantern Days</li>
      <li><svg viewBox="0 0 12 12"><circle cx="6" cy="6" r="6" fill="#6a5aa3"/><path d="M5,3.5L7.5,6L5,8.5" stroke="#fff" stroke-width="1.5" fill="none"/></svg>A day learning to re-align with your inner being <span class="price">£90</span></li>
    </ul>
    <p class="booking">Please book on line at <span class="booking__url">www.rosavale.co.uk</span></p>
    <div class="rule"></div>
    <footer class="contact-band">
      <span class="contact-band__item"><svg viewBox="0 0 16 16"><circle cx="8" cy="8" r="8" fill="#fff"/><rect x="4" y="5" width="8" height="6" fill="#5a4a94"/><path d="M4,5L8,8.5L12,5" stroke="#fff" fill="none" stroke-width="1"/></svg>rosa.vale@lanternmail.com</span>
      <span class="contact-band__item"><svg viewBox="0 0 16 16"><circle cx="8" cy="8" r="8" fill="#fff"/><path d="M5.5,4.5l1.5,0l0.8,2l-1,0.8c0.5,1,1.2,1.7,2.2,2.2l0.8-1l2,0.8l0,1.5c-3.5,0.5-7-3-6.3-6.3z" fill="#5a4a94"/></svg>01632 960418</span>
    </footer>
  </section>

</main>
</body>
</html>
```